Need Help having my business card stand out

I am the owner of Pine Ridge Canine Coaching and would like for my business cards to stand out. I have been trying to keep designing them myself but I can't get what I have in my head on the card. I will try my best to post templates that I like for inspirations. I want something unique but elegant. I don't want in to look cartoony or cheesy. It needs to pop in a pet shop but also in a coffee shop or gym.

Target Market(s)

Dog owners, Married ,No young kids Jr High school kids and up (maybe kids on the way) Executives, Stay at home moms/wives, Small business owners

Industry/Entity Type

Dog Training

Contact Information for Business Card

Trevor Holloway, 555-304-7162, info@pineridgecanine.example, www.pineridgecanine.example

Colors

Designer to choose colors to be used in the design.

Requirements
Must have
• my logo
Should not have
• Cursive lettering

```html
<!DOCTYPE html>
<html lang="en">
<head>
<meta charset="utf-8">
<title>Pine Ridge Canine Coaching – Business Card</title>
<link rel="stylesheet" href="https://fonts.googleapis.com/css2?family=Open+Sans:wght@400;600;700&display=swap">
<style>
  :root {
    --backdrop: #b9e2d6;
    --green: #6cb386;
    --green-soft: #cfe6d7;
    --green-pale: #eaf4ee;
    --ink: #1c1c1c;
    --paper: #ffffff;
    --night-1: #3a3a3a;
    --night-2: #0b0b0b;
    --muted: #4a4a4a;
  }
  html, body {
    margin: 0;
    width: 1200px;
    height: 856px;
    overflow: hidden;
    background: var(--backdrop);
    font-family: "Open Sans", sans-serif;
  }
  .canvas {
    position: relative;
    width: 1200px;
    height: 856px;
  }
  .card {
    position: absolute;
    left: 320px;
    width: 560px;
    height: 320px;
    border-radius: 26px;
    overflow: hidden;
    box-shadow: 0 10px 24px rgba(0, 0, 0, 0.18);
  }

  /* Front card */
  .card-front {
    top: 68px;
    background: var(--paper);
  }
  .front-pattern {
    position: absolute;
    right: 0;
    top: 0;
    width: 330px;
    height: 320px;
    background: linear-gradient(200deg, var(--green-soft) 0%, var(--green-pale) 45%, rgba(255,255,255,0) 80%);
  }
  .name-band {
    position: absolute;
    right: 0;
    top: 70px;
    width: 300px;
    height: 46px;
    background: linear-gradient(90deg, rgba(108,179,134,0) 0%, var(--green) 45%);
    color: var(--paper);
    text-align: right;
    padding-right: 28px;
    box-sizing: border-box;
  }
  .holder-name {
    display: block;
    font-weight: 700;
    font-size: 18px;
    line-height: 1;
    padding-top: 8px;
  }
  .holder-role {
    display: block;
    font-size: 11px;
    margin-top: 3px;
  }
  .brand-mark {
    position: absolute;
    left: 34px;
    top: 108px;
    display: flex;
    align-items: center;
    gap: 10px;
  }
  .brand-dot {
    width: 22px;
    height: 22px;
    border-radius: 50%;
    background: var(--ink);
  }
  .brand-name {
    font-weight: 700;
    font-size: 16px;
    color: var(--ink);
  }
  .contact-list {
    position: absolute;
    left: 34px;
    top: 170px;
    margin: 0;
    padding: 0;
    list-style: none;
    font-size: 12.5px;
    color: var(--muted);
  }
  .contact-list li {
    display: flex;
    align-items: flex-start;
    gap: 12px;
    margin-bottom: 9px;
    line-height: 1.5;
  }
  .contact-list svg {
    flex: none;
    margin-top: 3px;
  }

  /* Back card */
  .card-back {
    top: 460px;
    background: radial-gradient(circle at 62% 35%, var(--night-1) 0%, var(--night-2) 70%);
  }
  .back-brand {
    position: absolute;
    left: 44px;
    top: 92px;
    display: flex;
    align-items: center;
    gap: 14px;
    width: 260px;
  }
  .back-brand .brand-dot {
    width: 30px;
    height: 30px;
    background: var(--green);
  }
  .back-brand .brand-name {
    color: var(--green);
    font-size: 26px;
    line-height: 1.15;
  }
  .web-band {
    position: absolute;
    right: 0;
    top: 182px;
    width: 340px;
    height: 40px;
    background: var(--green);
    clip-path: polygon(8% 0, 100% 0, 100% 100%, 0 100%);
    color: var(--paper);
    font-weight: 700;
    font-size: 16px;
    line-height: 40px;
    text-align: right;
    padding-right: 26px;
    box-sizing: border-box;
  }
</style>
</head>
<body>
<main class="canvas">

  <section class="card card-front" aria-label="Business card front">
    <div class="front-pattern" role="img" aria-label="Soft green tiled grid decoration"></div>
    <div class="name-band">
      <span class="holder-name">Trevor Holloway</span>
      <span class="holder-role">Designation</span>
    </div>
    <div class="brand-mark">
      <span class="brand-dot"></span>
      <span class="brand-name">Pine Ridge Canine Coaching</span>
    </div>
    <ul class="contact-list">
      <li>
        <svg width="12" height="12" viewBox="0 0 12 12" aria-hidden="true"><path d="M6 0.5a4 4 0 0 0-4 4c0 3 4 7 4 7s4-4 4-7a4 4 0 0 0-4-4z" fill="#444"/><circle cx="6" cy="4.5" r="1.4" fill="#fff"/></svg>
        <span>#000 Example Street, Cedar Hollow,<br>Oregon, 00000, USA</span>
      </li>
      <li>
        <svg width="12" height="12" viewBox="0 0 12 12" aria-hidden="true"><path d="M2.5 1h2l1 3-1.5 1a7 7 0 0 0 3 3l1-1.5 3 1v2a1 1 0 0 1-1 1A9.5 9.5 0 0 1 1.5 2a1 1 0 0 1 1-1z" fill="#444"/></svg>
        <span>555-304-7162</span>
      </li>
      <li>
        <svg width="12" height="12" viewBox="0 0 12 12" aria-hidden="true"><rect x="0.5" y="2" width="11" height="8" rx="1" fill="#444"/><path d="M1 2.5l5 4 5-4" stroke="#fff" fill="none"/></svg>
        <span>info@pineridgecanine.example</span>
      </li>
      <li>
        <svg width="12" height="12" viewBox="0 0 12 12" aria-hidden="true"><circle cx="6" cy="6" r="5.3" fill="#444"/><path d="M0.8 6h10.4M6 0.8c-2.6 3-2.6 7.4 0 10.4M6 0.8c2.6 3 2.6 7.4 0 10.4" stroke="#fff" stroke-width="0.8" fill="none"/></svg>
        <span>www.pineridgecanine.example</span>
      </li>
    </ul>
  </section>

  <section class="card card-back" aria-label="Business card back">
    <div class="back-brand">
      <span class="brand-dot"></span>
      <span class="brand-name">Pine Ridge Canine Coaching</span>
    </div>
    <div class="web-band">www.pineridgecanine.example</div>
  </section>

</main>
</body>
</html>
```